Uprising SaaS company needs an attractive business card design

We're an uprising SaaS company who's attempting to attack the rigid car (insurance) claims management market in Europe.
We want to our mighty base order management system, listen to our clients to connect the smart ideas to build something even mightier.
We primarily focus on helping our customers manage their customers' claims/orders and get them resolved as smoothly as possible.
We'd like the business card design to express technical innovation and the fact that we connect smart ideas, as our company slogan indicates.
Contact Information for Business Card
Name, position, website, email, mobile, business address
Font styles to use
Colors
Designer to choose colors to be used in the design.
Look and feel
Each slider illustrates characteristics of the customer's brand and the style your logo design should communicate.

```html
<!DOCTYPE html>
<html lang="en">
<head>
<meta charset="utf-8">
<title>claimora – business card</title>
<link rel="stylesheet" href="https://fonts.googleapis.com/css2?family=Poppins:wght@300;400;600&display=swap">
<style>
  :root {
    --stage: #d9d9d9;
    --card-white: #ffffff;
    --ink-grey: #6f6f6f;
    --ink-soft: #7d7d7d;
    --accent-blue: #7ccde2;
    --grad-grey: #777777;
    --grad-blue: #80d0e4;
  }
  * { box-sizing: border-box; margin: 0; padding: 0; }
  html, body {
    width: 1200px; height: 852px; overflow: hidden;
    background: var(--stage);
    font-family: "Poppins", sans-serif;
  }
  .stage {
    width: 1200px; height: 852px;
    display: flex; flex-direction: column;
    align-items: center; justify-content: center; gap: 40px;
  }
  .card {
    position: relative;
    width: 660px; height: 377px;
    box-shadow: 0 6px 18px rgba(0,0,0,0.18);
    overflow: hidden;
  }
  /* Front side */
  .card--front {
    background:
      radial-gradient(ellipse at 78% 22%, var(--grad-blue) 0%, rgba(128,208,228,0.85) 30%, rgba(128,208,228,0) 72%),
      linear-gradient(35deg, var(--grad-grey) 35%, #86a9b3 70%, var(--grad-blue) 100%);
  }
  .front-brand {
    position: absolute; left: 44px; bottom: 48px;
    display: flex; align-items: center; gap: 10px;
    color: #ffffff; font-weight: 300; font-size: 40px; letter-spacing: 0.5px;
  }
  .front-brand .brand-dot {
    width: 10px; height: 10px; border-radius: 50%; background: #ffffff;
  }
  /* Back side */
  .card--back { background: var(--card-white); }
  .person {
    position: absolute; right: 48px; top: 34px; text-align: right;
  }
  .person-name { font-weight: 600; font-size: 19px; color: var(--ink-grey); }
  .person-role { font-weight: 400; font-size: 11px; color: var(--accent-blue); letter-spacing: 0.5px; }
  .back-brand {
    position: absolute; left: 52px; top: 118px;
    display: flex; align-items: center; gap: 12px;
    color: var(--ink-grey); font-weight: 300; font-size: 66px; letter-spacing: 1px;
  }
  .back-brand .brand-dot {
    width: 14px; height: 14px; border-radius: 50%; background: var(--accent-blue);
  }
  .divider {
    position: absolute; left: 52px; right: 48px; top: 212px; height: 3px;
  }
  .address {
    position: absolute; right: 48px; top: 228px; text-align: right;
    font-size: 13px; line-height: 1.5; color: var(--ink-soft);
  }
  .contact-rule {
    position: absolute; left: 52px; top: 282px; width: 150px; height: 3px;
  }
  .contacts {
    position: absolute; left: 52px; top: 292px; list-style: none;
    font-size: 13px; line-height: 1.6; color: var(--ink-soft);
  }
  .contacts li { display: flex; align-items: center; gap: 8px; }
  .contacts svg { width: 11px; height: 11px; fill: var(--accent-blue); }
</style>
</head>
<body>
<main class="stage">
  <section class="card card--front" aria-label="Card front">
    <div class="front-brand"><span>claimora</span><span class="brand-dot"></span></div>
  </section>

  <section class="card card--back" aria-label="Card back">
    <div class="person">
      <p class="person-name">Jonas Adler</p>
      <p class="person-role">CEO</p>
    </div>

    <div class="back-brand"><span>claimora</span><span class="brand-dot"></span></div>

    <svg class="divider" viewBox="0 0 560 3" preserveAspectRatio="none">
      <defs>
        <linearGradient id="rule-fade" x1="0" x2="1">
          <stop offset="0.3" stop-color="#6f6f6f"/>
          <stop offset="0.6" stop-color="#7ccde2"/>
        </linearGradient>
      </defs>
      <line x1="0" y1="1.5" x2="560" y2="1.5" stroke="url(#rule-fade)" stroke-width="2.5" stroke-dasharray="2.5 2.5"/>
    </svg>

    <address class="address" style="font-style: normal;">
      claimora GmbH<br>
      Lindenweg 14b<br>
      10115 Berlin - Germany
    </address>

    <svg class="contact-rule" viewBox="0 0 150 3" preserveAspectRatio="none">
      <line x1="0" y1="1.5" x2="150" y2="1.5" stroke="#6f6f6f" stroke-width="2.5" stroke-dasharray="2.5 2.5"/>
    </svg>

    <ul class="contacts">
      <li>
        <svg viewBox="0 0 24 24"><path d="M6.6 10.8a15.1 15.1 0 0 0 6.6 6.6l2.2-2.2a1 1 0 0 1 1-.25 11.4 11.4 0 0 0 3.6.57 1 1 0 0 1 1 1V20a1 1 0 0 1-1 1A17 17 0 0 1 3 4a1 1 0 0 1 1-1h3.5a1 1 0 0 1 1 1c0 1.25.2 2.45.57 3.57a1 1 0 0 1-.25 1z"/></svg>
        030.5550.1842
      </li>
      <li>
        <svg viewBox="0 0 24 24"><path d="M2 5h20v14H2z M2 5l10 8 10-8" /></svg>
        info@claimora.com
      </li>
      <li>
        <svg viewBox="0 0 24 24"><circle cx="12" cy="12" r="10"/><path d="M2 12h20M12 2c3 3 3 17 0 20M12 2c-3 3-3 17 0 20" stroke="#fff" stroke-width="1.6" fill="none"/></svg>
        www.claimora.com
      </li>
    </ul>
  </section>
</main>
</body>
</html>
```